Radiant Harvest Gathering 2021

I am looking to create a flyer for a one day prayer retreat our church is organizing. This flyer will be posted on social media, websites, mobile apps, and will also be printed so it can be mailed to people.

I am looking for something professional, with good use of our logo and band colors (logo colors).

I am counting on the designer's skill, creativity, art and knowledge of media communication to produce a flyer that will effectively and quickly convey the message we are trying to spread.

CONTENT OF THE FLYER:
Event title: Radiant Harvest Gathering
Date: Tuesday July 2nd, 2021
Time: 11:00AM - 7:00PM
Bellmore Hotel, 4817 Wexley Avenue, Portland, Maine 04109 (Room: Tamarind)
Event Key words to highlight what the event is about: Prayer, Fasting, Worship, Prophecy, Revival.
Key phrases:
A one day prayer retreat.
Jesus Chris is Lord

Contact info:
www.quvello.org
Phone: 207 555 0148
Email: contact@brookmeadow.org

```html
<!DOCTYPE html>
<html lang="en">
<head>
<meta charset="utf-8">
<title>Radiant Harvest Gathering 2021</title>
<link href="https://fonts.googleapis.com/css2?family=League+Gothic&family=Montserrat:wght@500;600&display=swap" rel="stylesheet">
<style>
  :root{
    --stage:#f6ead3;
    --ink:#262626;
    --orange:#f5941e;
    --white:#ffffff;
  }
  *{margin:0;padding:0;box-sizing:border-box}
  html,body{width:1200px;height:659px;overflow:hidden;background:var(--stage)}
  .flyer{position:absolute;left:365px;top:24px;width:470px;height:610px;background:var(--ink);overflow:hidden;
    font-family:"Montserrat",sans-serif;color:var(--white)}
  .abs{position:absolute}
  .hero-photo{left:0;top:0;width:330px;height:300px;
    background:radial-gradient(ellipse 130px 120px at 212px 128px,#d4d4d4 0%,#808080 32%,#3c3c3c 68%,var(--ink) 100%)}

  .title{font-family:"League Gothic",sans-serif;right:16px;text-align:right;line-height:1;white-space:nowrap;
    color:var(--white);transform-origin:top right}
  .title-1{top:24px;font-size:76px}
  .title-2{top:88px;font-size:100px;transform:scaleY(1.3)}
  .title-3{top:196px;font-size:76px;transform:scaleY(1.25)}

  .date-block{left:230px;top:281px;width:224px;height:64px;background:var(--orange);font-family:"League Gothic",sans-serif;
    text-align:right;padding:2px 6px 0 0;white-space:nowrap}
  .date-day{font-size:42px;line-height:38px;color:var(--white)}
  .date-full{font-size:24px;line-height:22px;color:var(--ink)}
  .time-bar{left:230px;top:351px;width:224px;height:44px;background:var(--orange);font-family:"League Gothic",sans-serif;
    font-size:42px;line-height:46px;text-align:center;color:var(--white);white-space:nowrap}

  .rule{height:1.5px;background:var(--orange);left:227px;width:227px}
  .venue-pin{left:227px;top:429px;width:47px;height:48px}
  .venue{left:283px;top:423px;font-size:13px;line-height:16px;font-weight:500;white-space:nowrap}
  .venue-room{color:var(--orange);font-size:11.5px}
  .program-title{left:227px;top:505px;font-size:17.5px;color:var(--orange);font-weight:500}
  .program-item{font-size:14px;font-weight:500;display:flex;align-items:center;gap:5px;letter-spacing:.3px}
  .program-item svg{width:16px;height:16px}

  .phrases-frame{left:16px;top:304px;width:202px;height:108px}
  .phrases-label{left:30px;top:297px;font-size:12px;color:var(--orange);font-weight:500;background:var(--ink);padding:0 3px}
  .phrase{left:26px;font-size:16px;font-weight:500;line-height:21px}
  .phrase-rule{left:26px;top:372px;width:24px;height:1px;background:var(--orange)}

  .org-mark{left:22px;top:478px;width:14px;height:14px;border-radius:50%;background:var(--orange)}
  .org-name{left:44px;top:460px;font-size:36px;font-weight:500;color:var(--white);letter-spacing:1px}

  .contact-box{left:12px;top:540px;width:202px;height:70px;background:var(--orange);padding:10px 0 0 8px}
  .contact-line{display:flex;align-items:center;gap:5px;font-size:12.5px;font-weight:500;line-height:16px;white-space:nowrap}
  .contact-line svg{width:9px;height:9px;flex:none}
</style>
</head>
<body>
<main class="flyer">
  <div class="abs hero-photo" role="img" aria-label="Black and white photo of hands folded in prayer on an open Bible before a lit cross"></div>

  <div class="abs title title-1">RADIANT</div>
  <div class="abs title title-2">HARVEST</div>
  <div class="abs title title-3">GATHERING</div>

  <div class="abs date-block">
    <div class="date-day">TUESDAY</div>
    <div class="date-full">JULY 2ND, 2021</div>
  </div>
  <div class="abs time-bar">11:00AM - 7:00PM</div>

  <div class="abs rule" style="top:413px"></div>
  <svg class="abs venue-pin" viewBox="0 0 47 48" aria-hidden="true">
    <path d="M23.5 4a12 12 0 0 0-12 12c0 9 12 22 12 22s12-13 12-22a12 12 0 0 0-12-12z" fill="none" stroke="var(--orange)" stroke-width="4"/>
    <circle cx="23.5" cy="16" r="4.5" fill="none" stroke="var(--orange)" stroke-width="3.5"/>
    <path d="M14 36c-8 1.5-11 4-9 6 3 3 34 3 37 0 2-2-1-4.5-9-6" fill="none" stroke="var(--orange)" stroke-width="3.5"/>
  </svg>
  <div class="abs venue">
    Bellmore Hotel,<br>
    4817 Wexley Avenue,<br>
    Portland, Maine 04109<br>
    <span class="venue-room">(Room: Tamarind)</span>
  </div>
  <div class="abs rule" style="top:494px"></div>

  <div class="abs program-title">Event Program:</div>
  <div class="abs program-item" style="left:227px;top:533px"><svg viewBox="0 0 16 16"><circle cx="8" cy="8" r="8" fill="var(--orange)"/><path d="M4.3 8.2l2.5 2.5 5-5" fill="none" stroke="var(--white)" stroke-width="2"/></svg>PRAYER</div>
  <div class="abs program-item" style="left:336px;top:533px"><svg viewBox="0 0 16 16"><circle cx="8" cy="8" r="8" fill="var(--orange)"/><path d="M4.3 8.2l2.5 2.5 5-5" fill="none" stroke="var(--white)" stroke-width="2"/></svg>FASTING</div>
  <div class="abs program-item" style="left:227px;top:556px"><svg viewBox="0 0 16 16"><circle cx="8" cy="8" r="8" fill="var(--orange)"/><path d="M4.3 8.2l2.5 2.5 5-5" fill="none" stroke="var(--white)" stroke-width="2"/></svg>WORSHIP</div>
  <div class="abs program-item" style="left:336px;top:556px"><svg viewBox="0 0 16 16"><circle cx="8" cy="8" r="8" fill="var(--orange)"/><path d="M4.3 8.2l2.5 2.5 5-5" fill="none" stroke="var(--white)" stroke-width="2"/></svg>PROPHECY</div>
  <div class="abs program-item" style="left:227px;top:579px"><svg viewBox="0 0 16 16"><circle cx="8" cy="8" r="8" fill="var(--orange)"/><path d="M4.3 8.2l2.5 2.5 5-5" fill="none" stroke="var(--white)" stroke-width="2"/></svg>REVIVAL</div>

  <svg class="abs phrases-frame" viewBox="0 0 202 108" aria-hidden="true">
    <path d="M0.6 0.6H146L201 107.4H0.6Z" fill="none" stroke="var(--white)" stroke-width="1.2"/>
  </svg>
  <div class="abs phrases-label">KEY PHRASES:</div>
  <div class="abs phrase" style="top:320px">A one day<br>prayer retreat.</div>
  <div class="abs phrase-rule"></div>
  <div class="abs phrase" style="top:380px">Jesus Chris is Lord</div>

  <div class="abs org-mark"></div>
  <div class="abs org-name">Quvello</div>

  <div class="abs contact-box">
    <div class="contact-line"><svg viewBox="0 0 10 10"><circle cx="5" cy="5" r="4.3" fill="none" stroke="var(--ink)" stroke-width="1.2"/></svg>207 555 0148</div>
    <div class="contact-line"><svg viewBox="0 0 10 10"><rect x="1" y="2.5" width="8" height="5" fill="var(--ink)"/></svg>www.quvello.org</div>
    <div class="contact-line"><svg viewBox="0 0 10 10"><circle cx="5" cy="5" r="4.3" fill="none" stroke="var(--ink)" stroke-width="1.2"/><path d="M1 5h8M5 1v8" stroke="var(--ink)" stroke-width=".9"/></svg>contact@brookmeadow.org</div>
  </div>
</main>
</body>
</html>
```